Adventurous female pilot

I am looking for a personal business card, for a very well qualified female pilot, with a lot of aviation experience.

Currently an airline pilot, have worked as a bush pilot in Africa, looking to get into corporate aviation, or private jet owners.
Want a classy looking card for networking...

Could be interested in a retro\vintage look also?!

An idea,, is an african sunset background, with my wings\logo on it
Updates

I just want to say thank you to all of your for your amazing designs!

I have been very busy flying this past week , so not had a chance to be on the computer much.
But I provide some feedback, and conclusions very soon!
Thank you again.

Marla

Reason: Still waiting on a couple of revisions to be 100% about my choice!

Target Market(s)

corporate aviation, private jet owners, casino's,
General audience.
networking

Industry/Entity Type

Airline

Requirements
Nice to have
• Classy, edgy, sexy, but also feminine

```html
<!DOCTYPE html>
<html lang="en">
<head>
<meta charset="utf-8">
<title>Marla Vance – Pilot</title>
<link href="https://fonts.googleapis.com/css2?family=Great+Vibes&family=Open+Sans:ital,wght@0,400;0,600;0,700;1,400&display=swap" rel="stylesheet">
<style>
  :root {
    --glow-core: #fff200;
    --glow-mid: #e3b400;
    --amber: #c9841c;
    --rust: #8c3f1c;
    --rust-deep: #863a1a;
    --horizon: #d2782a;
    --earth-dark: #1e120b;
    --ink: #2a1e10;
    --white: #ffffff;
    --label-yellow: #ffee00;
  }
  * { margin: 0; padding: 0; box-sizing: border-box; }
  html, body {
    width: 676px;
    height: 1200px;
    overflow: hidden;
    background: #ffffff;
  }
  .card {
    position: relative;
    width: 676px;
    height: 1200px;
    overflow: hidden;
    background:
      radial-gradient(ellipse 470px 360px at 50% 15%, var(--glow-core) 0%, var(--glow-mid) 30%, var(--amber) 55%, rgba(140,63,28,0) 100%),
      linear-gradient(to bottom, var(--amber) 0%, var(--rust) 38%, var(--rust-deep) 68%, var(--horizon) 88%, var(--horizon) 100%);
    font-family: "Open Sans", Arial, sans-serif;
  }
  .brand {
    position: absolute;
    top: 110px;
    left: 0;
    width: 100%;
    text-align: center;
    color: var(--ink);
  }
  .brand-dot {
    display: block;
    width: 34px;
    height: 34px;
    margin: 0 auto 88px;
    border-radius: 50%;
    background: var(--ink);
  }
  .brand-name {
    font-family: "Open Sans", Arial, sans-serif;
    font-weight: 600;
    font-size: 29px;
    line-height: 36px;
    letter-spacing: 0.5px;
  }
  .person {
    position: absolute;
    top: 522px;
    left: 0;
    width: 100%;
    text-align: center;
    color: var(--white);
  }
  .person-name {
    font-family: "Great Vibes", cursive;
    font-weight: 400;
    font-size: 78px;
    line-height: 88px;
  }
  .person-role {
    font-style: italic;
    font-size: 30px;
    line-height: 36px;
    margin-top: -8px;
  }
  .contact {
    position: absolute;
    top: 846px;
    left: 118px;
    list-style: none;
    color: var(--white);
    font-size: 28px;
    line-height: 43px;
  }
  .contact-label {
    color: var(--label-yellow);
    font-weight: 700;
  }
  .savanna {
    position: absolute;
    left: 0;
    bottom: 0;
    width: 676px;
    height: 170px;
    background: linear-gradient(to bottom, rgba(30,18,11,0) 0%, rgba(30,18,11,0.55) 45%, var(--earth-dark) 100%);
  }
</style>
</head>
<body>
  <main class="card">
    <header class="brand">
      <span class="brand-dot"></span>
      <p class="brand-name">MARLA VANCE AVIATION</p>
    </header>

    <section class="person">
      <h1 class="person-name">Marla Vance</h1>
      <p class="person-role">Pilot</p>
    </section>

    <ul class="contact">
      <li><span class="contact-label">Email:</span> marla.vance@skyrover.net</li>
      <li><span class="contact-label">Cell US:</span> +1 702-555-0148</li>
      <li><span class="contact-label">Cell Taipei:</span> +886 900-555-218</li>
    </ul>

    <div class="savanna" role="img" aria-label="Silhouettes of acacia trees, elephants, giraffes and a zebra on the African savanna at sunset"></div>
  </main>
</body>
</html>
```